Harbor Ridge Elementary School Letterhead

We would like a letterhead that includes our school mascot (Flicker the Falcon), school address, and phone number. We want something with personality and a little fun. Our school colors are navy blue, green (like the flag in our graphic), and gray. We included an example of a letterhead we like the feel of (on the fun side). The example is the image titled "sample." We are the Harbor Ridge Falcons.
Harbor Ridge Elementary
Address: 418 Marlow Fern, Irvine, CA 92781
Phone: (949) 555-0174
harborridge.oksd.example
Target Market(s)
Elementary School Families

```html
<!DOCTYPE html>
<html lang="en">
<head>
<meta charset="utf-8">
<title>Harbor Ridge Elementary – Letterhead</title>
<link href="https://fonts.googleapis.com/css2?family=Lato:wght@300;400;700;900&family=Open+Sans:wght@400&family=Great+Vibes&display=swap" rel="stylesheet">
<style>
  :root {
    --backdrop: #e6e6e6;
    --paper: #f2f2f2;
    --ink: #3a3a3a;
    --ink-strong: #111111;
    --ink-soft: #555555;
    --bar-gray: #7d7d7d;
    --school-navy: #1f2f5c;
    --school-green: #3a9a4a;
    --watermark: rgba(31, 47, 92, 0.035);
  }
  * { margin: 0; padding: 0; box-sizing: border-box; }
  html, body {
    width: 1200px; height: 1200px; overflow: hidden;
    background: var(--backdrop);
  }
  .letterhead {
    position: absolute; left: 211px; top: 50px;
    width: 778px; height: 1100px;
    background: var(--paper);
    font-family: "Lato", sans-serif;
    color: var(--ink);
    overflow: hidden;
  }
  .top-bar {
    position: absolute; left: 0; top: 0; width: 100%; height: 10px;
    background: linear-gradient(90deg, #8a8a8a, #d8d8d8 45%, #d8d8d8 60%, #8a8a8a);
  }
  .brand {
    position: absolute; left: 49px; top: 46px; height: 72px;
    display: flex; align-items: center; gap: 10px;
  }
  .brand-dot {
    width: 72px; height: 72px; border-radius: 50%;
    background: var(--school-navy);
  }
  .brand-name {
    font-family: "Lato", sans-serif; font-weight: 900;
    font-size: 22px; line-height: 1.05; color: var(--school-navy);
    text-transform: uppercase;
  }
  .watermark-mascot {
    position: absolute; left: 204px; top: 350px; width: 383px; height: 400px;
    border-radius: 46% 50% 44% 48%;
    background: radial-gradient(circle at 50% 45%, var(--watermark), rgba(31,47,92,0.015) 70%, transparent 72%);
  }
  .letter-body {
    position: absolute; left: 83px; top: 240px; width: 612px;
    font-size: 12.8px; font-weight: 300; line-height: 18.3px;
  }
  .date { margin-bottom: 18.3px; }
  .recipient { margin-bottom: 36.6px; }
  .recipient strong { font-weight: 700; color: var(--ink-strong); }
  .greeting { margin-bottom: 18.3px; }
  .letter-body p.copy { text-align: justify; margin-bottom: 18.3px; }
  .closing { margin-top: 55px; }
  .signature {
    font-family: "Great Vibes", cursive; font-size: 27px;
    color: var(--ink-strong); margin: 6px 0 0 6px; line-height: 1.2;
  }
  .footer-rule {
    position: absolute; left: 49px; top: 1027px; width: 27px; height: 3px;
    background: var(--bar-gray);
  }
  .contact {
    position: absolute; left: 49px; top: 1040px;
    font-family: "Open Sans", sans-serif; font-size: 11.5px; color: var(--ink-soft);
    line-height: 16px; list-style: none;
  }
  .contact li { display: flex; align-items: center; gap: 4px; }
  .contact svg { width: 9px; height: 9px; fill: var(--school-navy); }
  .mascot-illustration {
    position: absolute; left: 588px; top: 978px; width: 143px; height: 122px;
    border-radius: 40% 40% 30% 30%;
    background: linear-gradient(135deg, #9a9a9a, #d4d4d4 55%, var(--school-green));
  }
  .bottom-bar {
    position: absolute; left: 0; bottom: 0; width: 100%; height: 10px;
    background: linear-gradient(90deg, var(--bar-gray) 0 658px, var(--school-navy) 658px);
  }
</style>
</head>
<body>
  <article class="letterhead">
    <div class="top-bar"></div>

    <header class="brand">
      <span class="brand-dot"></span>
      <span class="brand-name">Harbor Ridge<br>Falcons</span>
    </header>

    <div class="watermark-mascot" role="img" aria-label="Faint large school mascot artwork behind the letter text"></div>

    <section class="letter-body">
      <p class="date">01 January 2050</p>
      <p class="recipient"><strong>Company (Pvt) Ltd.</strong><br>PO Box 3355 Mainville St<br>Sample City Country 3355</p>
      <p class="greeting">Dear Nolan Averly,</p>
      <p class="copy">Lorem ipsum dolor sit amet, consectetuer adipiscing elit, sed diam nonummy nibh euismod tincidunt ut laoreet dolore magna aliquam erat volutpat. Ut wisi enim ad minim veniam, quis nostrud exerci tation ullamcorper suscipit lobortis nisl ut aliquip ex ea commodo consequat. Duis dolore te feugait nulla facilisi. Nam liber tempor cum soluta nobis eleifend option congue nihil imperdiet doming id quod mazim placerat facer possim assum. Lorem ipsum dolor sit amet, consectetuer adipiscing elit, sed diam nonummy nibh euismod tincidunt ut laoreet dolore magna aliquam erat volutpat. Ut wisi enim ad minim veniam, quis nostrud exerci tation ullamcorper suscipit lobortis nisl ut aliquip ex ea commodo consequat.</p>
      <p class="copy">Consectetuer adipiscing elit, sed diam nonummy nibh euismod tincidunt ut laoreet dolore magna aliquam erat volutpat. Ut wisi enim ad minim veniam, quis nostrud exerci tation ullamcorper suscipit lobortis nisl ut aliquip ex ea commodo consequat. Consectetuer adipiscing elit, sed diam nonummy nibh euismod tincidunt ut laoreet dolore magna aliquam erat volutpat. Ut wisi enim ad minim veniam, quis nostrud exerci tation ullamcorper suscipit lobortis nisl ut aliquip ex ea commodo consequat.</p>
      <p class="copy">Consectetuer adipiscing elit, sed diam nonummy nibh euismod tincidunt ut laoreet dolore magna aliquam erat volutpat. Ut wisi enim ad minim veniam, quis nostrud exerci tation ullamcorper suscipit lobortis nisl ut aliquip ex ea commodo consequat. Consectetuer adipiscing elit, sed diam nonummy nibh euismod tincidunt ut laoreet dolore magna aliquam erat volutpat. Ut wisi enim ad minim veniam, quis nostrud exerci tation ullamcorper suscipit lobortis nisl ut aliquip ex ea commodo consequat.</p>
      <p class="closing">Sincerely Yours</p>
      <p class="signature">Miriam Lowell Parrish</p>
    </section>

    <div class="footer-rule"></div>
    <ul class="contact">
      <li>
        <svg viewBox="0 0 24 24" aria-hidden="true"><path d="M6.6 10.8a15 15 0 0 0 6.6 6.6l2.2-2.2c.3-.3.7-.4 1-.2 1.1.4 2.3.6 3.6.6.6 0 1 .4 1 1V20c0 .6-.4 1-1 1A17 17 0 0 1 3 4c0-.6.4-1 1-1h3.5c.6 0 1 .4 1 1 0 1.3.2 2.5.6 3.6.1.3 0 .7-.2 1z"/></svg>
        (949) 555-0174
      </li>
      <li>
        <svg viewBox="0 0 24 24" aria-hidden="true"><path d="M12 2a7 7 0 0 0-7 7c0 5.2 7 13 7 13s7-7.8 7-13a7 7 0 0 0-7-7zm0 9.5A2.5 2.5 0 1 1 12 6.5a2.5 2.5 0 0 1 0 5z"/></svg>
        418 Marlow Fern, Irvine, CA 92781
      </li>
    </ul>

    <div class="mascot-illustration" role="img" aria-label="Cartoon school mascot holding a green flag"></div>
    <div class="bottom-bar"></div>
  </article>
</body>
</html>
```